SOLVEN TRIDE PORTAL

I'D LIKE TO REDESIGN MY WEBSITE TO MATCH WITH THE NEW BROCHURE WHICH IS ATTACHED. CONTENT AND LOGOS ARE ATTACHED. PLEASE USE WATCH BRAND LOGOS FROM THE BROCHURE
Coded - Design and coding required
1 page

```html
<!DOCTYPE html>
<html lang="en">
<head>
<meta charset="utf-8">
<title>Solven Tride Portal</title>
<link rel="stylesheet" href="https://fonts.googleapis.com/css2?family=Bellefair&family=Marcellus&family=Poppins:wght@400;500;600&display=swap">
<style>
:root{
  --black:#000;
  --panel:#1b1b1b;
  --panel-dark:#141414;
  --form-box:#232323;
  --gold:#b8993a;
  --gold-line:#c9a43a;
  --white:#fff;
  --muted:#cfcfcf;
  --field-border:#bbb;
  --placeholder:#9a9a9a;
}
*{box-sizing:border-box;margin:0;padding:0}
html,body{width:1200px;height:4571px;overflow:hidden;background:var(--black)}
body{position:relative;font-family:"Poppins",sans-serif;color:var(--white)}
.abs{position:absolute}

/* hero */
.hero{left:0;top:0;width:1200px;height:737px;background:radial-gradient(ellipse at 45% 40%,#4a4a4a 0%,#262626 45%,#0a0a0a 85%)}
.brand{left:107px;top:30px;display:flex;align-items:center;gap:10px}
.brand-mark{width:44px;height:44px;background:var(--gold)}
.brand-name{font-family:"Bellefair",serif;font-size:14px;color:var(--gold);letter-spacing:1px;width:110px;line-height:1.2}
.nav{top:45px;right:93px;display:flex;gap:26px;font-size:16px}
.hero-title{left:0;width:1200px;top:175px;text-align:center;font-family:"Bellefair",serif;font-size:38px;line-height:46px;font-weight:400}
.hero-copy{left:225px;width:750px;top:309px;text-align:center;font-size:12.5px;line-height:19px}
.hero-tag{left:0;width:1200px;top:414px;text-align:center;font-size:16px}
.arrow{top:503px}
.thumb{top:497px;width:75px;height:75px}
.brands{left:135px;top:694px;width:930px;height:87px;background:var(--white);display:flex;align-items:center;justify-content:space-around;color:#111}
.brands span{font-family:"Bellefair",serif;font-size:24px}

/* about */
.about-h{left:100px;top:823px;font-family:"Bellefair",serif;font-size:42px;letter-spacing:10px;font-weight:400}
.about-sub{left:97px;top:895px;font-family:"Bellefair",serif;font-size:30px;letter-spacing:8px}
.prose{font-family:"Marcellus",serif;font-size:26px;line-height:45px}

/* sections */
.invest{left:0;top:2663px;width:1200px;height:376px;background:var(--panel)}
.sourcing{left:0;top:3039px;width:1200px;height:852px;background:var(--panel-dark)}
.contact{left:0;top:3891px;width:1200px;height:614px;background:var(--panel)}
.footer{left:0;top:4505px;width:1200px;height:66px;background:#101010;text-align:center;font-family:"Bellefair",serif;font-size:18px;line-height:66px}
.sec-title{left:0;width:1200px;text-align:center;font-family:"Bellefair",serif;font-size:28px;font-weight:400}
.rule{height:2px;background:var(--gold-line)}
.btn{background:var(--gold);color:#111;font-size:13px;font-weight:600;display:flex;align-items:center;justify-content:center;border-radius:3px}
.label{font-size:11px}
.field{background:var(--white);border:1px solid var(--field-border);font-size:12px;color:var(--placeholder);padding:0 10px;display:flex;align-items:center}
.field.select{justify-content:space-between}
.field.area{align-items:flex-start;padding-top:14px}
.form-box{left:138px;top:3971px;width:426px;height:452px;background:var(--form-box)}
.c-label{left:175px;font-size:11px}
.c-field{left:169px;width:364px;height:36px;background:var(--white);border-radius:3px;color:#333;font-size:12px;padding:0 12px;display:flex;align-items:center}
.contact-line{left:660px;font-size:14px;display:flex;align-items:center;gap:12px}
.social{top:4336px;display:flex;gap:14px;left:668px;font-size:14px}
.social span{display:flex;align-items:center;gap:5px}
.dot{width:10px;height:10px;border-radius:50%;background:var(--white)}
</style>
</head>
<body>

<section class="abs hero" role="img" aria-label="Close-up of a luxury diver watch dial in dark tones"></section>
<div class="abs brand"><div class="brand-mark"></div><div class="brand-name">SOLVEN TRIDE PORTAL</div></div>
<nav class="abs nav"><span>Home</span><span>About</span><span>Investments</span><span>Search Watches</span><span>Contact</span></nav>
<h1 class="abs hero-title">Welcome to Solven Tride Portal<br>International luxury timepiece supplier</h1>
<p class="abs hero-copy">Simply choose a desired product and allow us to source it for you at the best price and with suitable delivery terms. You will have an option to either collect your purchase from our Cheshire based boutique store, collection points are also in New York City or Dubai or get it delivered to your door via one of our fully insured couriers.</p>
<p class="abs hero-tag">Making your luxury shopping experience as simple as it can be.</p>
<svg class="abs arrow" style="left:138px" width="105" height="60" viewBox="0 0 105 60"><path d="M103 30H4M30 4L4 30l26 26" stroke="#fff" stroke-width="4" fill="none"/></svg>
<svg class="abs arrow" style="left:947px" width="105" height="60" viewBox="0 0 105 60"><path d="M2 30h99M75 4l26 26-26 26" stroke="#fff" stroke-width="4" fill="none"/></svg>
<div class="abs thumb" style="left:310px;background:linear-gradient(135deg,#1fb5c9,#d8d8d8)" role="img" aria-label="Watch on teal background"></div>
<div class="abs thumb" style="left:409px;background:linear-gradient(180deg,#d77a4a,#2e2e3a)" role="img" aria-label="Watch at sunset"></div>
<div class="abs thumb" style="left:508px;background:linear-gradient(135deg,#7a5a3a,#1a1a1a)" role="img" aria-label="Watch on dark wood"></div>
<div class="abs thumb" style="left:607px;background:linear-gradient(135deg,#c33,#2a1a1a)" role="img" aria-label="Watch with red accents"></div>
<div class="abs thumb" style="left:706px;background:linear-gradient(135deg,#9a9a9a,#2a2a2a)" role="img" aria-label="Silver watch"></div>
<div class="abs thumb" style="left:805px;background:linear-gradient(135deg,#555,#0e0e0e)" role="img" aria-label="Black watch"></div>
<div class="abs brands"><span>HALDEN</span><span>MERIVO</span><span>ARDENCE</span><span>TOLLARD</span><span>BRISKWELL</span></div>

<h2 class="abs about-h">ABOUT</h2>
<p class="abs about-sub">Solven-Tride</p>
<p class="abs prose" style="left:97px;top:968px;width:515px">Solven Tride Portal was first founded in 2018, it has been established as the premier resource to buy and sell premium pre-owned watches. With thousands of watches available from brands including Merivo, Quenby, Ardence, Larrow, Tollard, Dunmere and more, plus international locations and clients there's no better place to find a luxury timepiece.</p>
<div class="abs" style="left:641px;top:960px;width:463px;height:476px;background:linear-gradient(135deg,#bdbdbd,#3c3c3c)" role="img" aria-label="Black and white photo of a chronograph watch on a wrist"></div>
<div class="abs" style="left:169px;top:1527px;width:390px;height:443px;background:radial-gradient(circle,#6a6a6a 0%,#1e1e1e 55%,#000 80%)" role="img" aria-label="Dark watch face surrounded by splashing water"></div>
<p class="abs prose" style="left:586px;top:1585px;width:520px">Outstanding customer service is a mainstay of the Solven-Tride ethos. Watch collectors are discerning shoppers, and will accept nothing but the best, which is why customer service has and always will be such an important part of the business.</p>
<p class="abs prose" style="left:97px;top:2100px;width:520px">Our dedicated team of swiss watch experts are perfectly placed to adapt to the ever changing market conditions, giving our investors an 'out of the box' solution. Longevity is as much a focus as immediate success, ensuring you have the best options we can provide tomorrow as well as</p>
<div class="abs" style="left:641px;top:2080px;width:463px;height:441px;background:linear-gradient(135deg,#2a3550,#0e1424)" role="img" aria-label="White-dial watch with leather strap resting on navy fabric"></div>

<section class="abs invest"></section>
<h2 class="abs sec-title" style="top:2716px">Investmets</h2>
<div class="abs rule" style="left:532px;top:2770px;width:136px"></div>
<p class="abs" style="left:0;width:1200px;top:2806px;text-align:center;font-family:'Marcellus',serif;font-size:23px">Interested in becoming part of the ever growing Solven-Tride Portal?</p>
<p class="abs" style="left:0;width:1200px;top:2860px;text-align:center;font-size:19px">Please leave your details&nbsp; and one of the team will be in touch to discuss potential options.</p>
<div class="abs btn" style="left:504px;top:2938px;width:158px;height:48px">Fill The Form</div>

<section class="abs sourcing"></section>
<h2 class="abs sec-title" style="top:3090px">Sourcing your Watch</h2>
<div class="abs rule" style="left:474px;top:3144px;width:252px"></div>
<p class="abs" style="left:0;width:1200px;top:3184px;text-align:center;font-size:19px">Fill the form please</p>
<span class="abs label" style="left:140px;top:3249px">Watch Brand</span>
<div class="abs field" style="left:140px;top:3270px;width:474px;height:44px">Full Name</div>
<span class="abs label" style="left:657px;top:3249px">Year</span>
<div class="abs field select" style="left:657px;top:3270px;width:383px;height:44px">Year<svg width="14" height="10" viewBox="0 0 14 10"><path d="M2 2l5 5 5-5" stroke="#333" stroke-width="2" fill="none"/></svg></div>
<span class="abs label" style="left:140px;top:3372px">Bezel</span>
<div class="abs field" style="left:140px;top:3392px;width:279px;height:46px">Bezel</div>
<span class="abs label" style="left:460px;top:3372px">Strap</span>
<div class="abs field" style="left:460px;top:3392px;width:247px;height:46px">Strap Size</div>
<span class="abs label" style="left:769px;top:3372px">Material</span>
<div class="abs field select" style="left:769px;top:3392px;width:259px;height:46px">Material Type<svg width="14" height="10" viewBox="0 0 14 10"><path d="M2 2l5 5 5-5" stroke="#333" stroke-width="2" fill="none"/></svg></div>
<span class="abs label" style="left:140px;top:3522px">Email Address</span>
<div class="abs field area" style="left:140px;top:3543px;width:893px;height:220px">Your Message</div>
<div class="abs btn" style="left:877px;top:3795px;width:158px;height:46px">Submit</div>

<section class="abs contact"></section>
<div class="abs form-box"></div>
<span class="abs c-label" style="top:4008px">Full Name</span>
<div class="abs c-field" style="top:4033px">Maren Holt</div>
<span class="abs c-label" style="top:4084px">Email Address</span>
<div class="abs c-field" style="top:4107px">maren@example.com</div>
<span class="abs c-label" style="top:4159px">Subject</span>
<div class="abs c-field" style="top:4182px">Upgrade current Plan</div>
<span class="abs c-label" style="top:4234px">What are you contacting for?</span>
<div class="abs c-field" style="top:4255px;height:71px;align-items:flex-start;padding-top:10px">Description</div>
<div class="abs c-field" style="top:4345px;justify-content:center;color:#555">Send</div>

<h2 class="abs" style="left:660px;top:3984px;font-family:'Bellefair',serif;font-size:28px;font-weight:400">Connect with Us</h2>
<div class="abs contact-line" style="top:4075px"><svg width="18" height="18" viewBox="0 0 18 18"><path d="M9 2C4.6 2 1 4.9 1 8.5c0 1.8.9 3.4 2.4 4.6L2.5 16l3.6-1.8c.9.3 1.9.5 2.9.5 4.4 0 8-2.9 8-6.5S13.4 2 9 2z" fill="#fff"/></svg>Call Us : 1800-000-4321</div>
<div class="abs contact-line" style="top:4118px"><svg width="18" height="18" viewBox="0 0 18 18"><rect x="1" y="4" width="16" height="11" fill="#fff"/><path d="M1 4l8 6 8-6" stroke="#1b1b1b" stroke-width="1.5" fill="none"/></svg>Email: sales@solventride-portal.example</div>
<div class="abs contact-line" style="top:4161px"><svg width="18" height="18" viewBox="0 0 18 18"><path d="M9 1a5 5 0 0 0-5 5c0 4 5 10 5 10s5-6 5-10a5 5 0 0 0-5-5z" fill="#fff"/><circle cx="9" cy="6" r="1.8" fill="#1b1b1b"/></svg>Address: TBC</div>
<p class="abs" style="left:660px;top:4228px;width:400px;font-size:13px;line-height:21px">Alternatively please feel free to contact us on 01610000000 For a more detailed chat with one of our timepiece specialists</p>
<div class="abs social"><span><i class="dot"></i>Folio</span><span><i class="dot"></i>Chirp</span><span><i class="dot"></i>Pinboard</span></div>

<footer class="abs footer">All right reserve to Solven Tride</footer>
</body>
</html>
```